Bref créative
Lark Hollow Events Business Cards & Stationary
A focus on events. All of them. All aspects of them. Anywhere.
I need double sided standard sized Business Card [3.5" x 2"]
Century Gothic
Professional
Melissa Dorne
CEO or would also like to try putting a function like "meetings + events"
4172 County Road 208
Medina, MN 55340
melissa@larkhollowevents.example
www.larkhollowevents.example
Info on who we are and what we do can be found on our website at www.larkhollowevents.example
Would like to see different options like:
phone.
cell.
email.
also, would like to see some options with this symbol: |
Like:
melissa dorne | lark hollow events
Would like to see the card with and without title.
Also, like the + symbol.
I'd like our business cards to look hip and professional...but want them to have some personality.
Our branding colors are gray, teal, and white. Open to incorporting another sub color as you see fit--possibly taupe, navy, or dark fuscia.
Hoping to see innovative ideas on what is up-and-coming with business cards now for people to take notice.
Our logo is new so we are interested in unique ways to use it.
I would like to try to fit this explanation about our name on the back because I love it. I know this will be tight--do what you need to if you need to cut out a little to get it to fit....but lets see if we can do this on the back. (Or, we could go to the fold-out kind if we have to and then do ubllets of our services on the back.)
In the 1950’s, doctors developed a personality classification that was supposed to help them identify predicators for heart disease. They grouped certain criteria together and labeled that personality, “Type A”. The term has come to have some negative connotations.
From our point of view, while we are an eclectic team of varied personalities and interests, we endeavor to provide type A service.
Does that make us a group of unlikable, over-bearing maniacs? No.
We think the so-called “symptoms” of type A are the same qualifications you want in your event planners:
Type A individuals can be described as time-conscious, competitive, ambitious, business-like perfectionists. They are usually over-achievers who derive a great deal of satisfaction from work and multi-tasking. They drive themselves with deadlines and are often “stress junkies”.
–Quiet Engines: Habits of the Restless Mind, Harold Vance
We proudly don the scarlet letter as a badge of our undying need to deliver services to you on time, in budget, and beyond your expectations. If that ends up leading to heart disease….well, we’ll live with that. If our service prevents your heart attacks, then we’ve done our job.
The colors of the logos are very close but still not quite hitting the mark--the gray is a little greenish and the teal is a little blah. When you're using them, please try other shades of gray and teal.
here is the eps version instead of ai in case that is desireable

```html
<!DOCTYPE html>
<html lang="en">
<head>
<meta charset="utf-8">
<title>Lark Hollow Events – Business Card Options</title>
<link href="https://fonts.googleapis.com/css2?family=Questrial&family=Libre+Baskerville&display=swap" rel="stylesheet">
<style>
  :root{
    --bg:#f4f4f3;
    --bg-edge:#c9c9c7;
    --label:#8a8a88;
    --card:#ffffff;
    --teal:#1b4753;
    --teal-light:#2a5d69;
    --taupe:#7b765f;
    --taupe-light:#8e8a74;
    --name:#3d5e66;
    --name-taupe:#5e5a47;
    --muted:#8d8d8d;
    --body:#595959;
    --white:#ffffff;
  }
  *{margin:0;padding:0;box-sizing:border-box}
  html,body{width:1200px;height:857px;overflow:hidden}
  body{
    position:relative;
    background:radial-gradient(ellipse 75% 70% at 50% 45%, var(--bg) 55%, var(--bg-edge) 100%);
    font-family:"Questrial", "Century Gothic", sans-serif;
  }
  .side-label{
    position:absolute;
    font-family:"Libre Baskerville", serif;
    font-size:27px;
    letter-spacing:2px;
    color:var(--label);
  }
  .card{
    position:absolute;
    width:504px;height:288px;
    background:var(--card);
    box-shadow:0 14px 18px -8px rgba(0,0,0,.35), 0 2px 6px rgba(0,0,0,.12);
    overflow:hidden;
  }
  .card-front{display:flex}
  .brand-panel{
    width:228px;height:100%;
    display:flex;align-items:center;justify-content:center;
  }
  .brand-panel.teal{background:linear-gradient(160deg,var(--teal-light),var(--teal))}
  .brand-panel.taupe{background:linear-gradient(160deg,var(--taupe-light),var(--taupe))}
  .brand-name{
    color:var(--white);
    font-size:15px;
    letter-spacing:2px;
    text-transform:uppercase;
    display:flex;align-items:center;gap:9px;
  }
  .brand-mark{width:12px;height:12px;background:var(--white)}
  .contact{padding:72px 0 0 38px}
  .person-name{font-size:23px;color:var(--name)}
  .taupe-card .person-name{color:var(--name-taupe)}
  .person-title{font-size:11px;color:var(--muted);margin-top:3px}
  .details{margin-top:40px;font-size:11px;line-height:14px;color:var(--name)}
  .taupe-card .details{color:var(--name-taupe)}
  .card-back{padding:26px 34px 0 34px;color:var(--body);font-size:6.6px;line-height:9px}
  .card-back p{margin-bottom:7px}
</style>
</head>
<body>
  <div class="side-label" style="left:240px;top:18px">FRONT</div>
  <div class="side-label" style="left:820px;top:18px">BACK</div>
  <div class="side-label" style="left:240px;top:446px">FRONT</div>
  <div class="side-label" style="left:820px;top:446px">BACK</div>

  <section class="card card-front" style="left:72px;top:84px">
    <div class="brand-panel teal"><div class="brand-name"><span class="brand-mark"></span>Lark Hollow Events</div></div>
    <div class="contact">
      <div class="person-name">Melissa Dorne</div>
      <div class="person-title">CEO</div>
      <div class="details">
        4172 County Road 208 Medina,<br>MN 55340<br>P: 763 555 0142<br>C: 612 555 0187<br>F: 763 555 0163<br>E: melissa@larkhollowevents.example<br>www.larkhollowevents.example
      </div>
    </div>
  </section>

  <section class="card card-back" style="left:618px;top:84px">
    <p>In the 1950’s, doctors developed a personality classification that was supposed to help them identify predicators for heart disease. They grouped certain criteria together and labeled that personality, “Type A”. The term has come to have some negative connotations.</p>
    <p>From our point of view, while we are an eclectic team of varied personalities and interests, we endeavor to provide type A service.</p>
    <p>Does that make us a group of unlikable, over-bearing maniacs? No.</p>
    <p>We think the so-called “symptoms” of type A are the same qualifications you want in your event planners:</p>
    <p>Type A individuals can be described as time-conscious, competitive, ambitious, business-like perfectionists. They are usually over-achievers who derive a great deal of satisfaction from work and multi-tasking. They drive themselves with deadlines and are often “stress junkies”.<br>–Quiet Engines: Habits of the Restless Mind, Harold Vance</p>
    <p>We proudly don the scarlet letter as a badge of our undying need to deliver services to you on time, in budget, and beyond your expectations. If that ends up leading to heart disease….well, we’ll live with that. If our service prevents your heart attacks, then we’ve done our job.</p>
  </section>

  <section class="card card-front taupe-card" style="left:72px;top:504px">
    <div class="brand-panel taupe"><div class="brand-name"><span class="brand-mark"></span>Lark Hollow Events</div></div>
    <div class="contact">
      <div class="person-name">Melissa Dorne</div>
      <div class="person-title">CEO</div>
      <div class="details">
        4172 County Road 208 Medina,<br>MN 55340<br>P: 763 555 0142<br>C: 612 555 0187<br>F: 763 555 0163<br>E: melissa@larkhollowevents.example<br>www.larkhollowevents.example
      </div>
    </div>
  </section>

  <section class="card card-back" style="left:618px;top:504px">
    <p>In the 1950’s, doctors developed a personality classification that was supposed to help them identify predicators for heart disease. They grouped certain criteria together and labeled that personality, “Type A”. The term has come to have some negative connotations.</p>
    <p>From our point of view, while we are an eclectic team of varied personalities and interests, we endeavor to provide type A service.</p>
    <p>Does that make us a group of unlikable, over-bearing maniacs? No.</p>
    <p>We think the so-called “symptoms” of type A are the same qualifications you want in your event planners:</p>
    <p>Type A individuals can be described as time-conscious, competitive, ambitious, business-like perfectionists. They are usually over-achievers who derive a great deal of satisfaction from work and multi-tasking. They drive themselves with deadlines and are often “stress junkies”.<br>–Quiet Engines: Habits of the Restless Mind, Harold Vance</p>
    <p>We proudly don the scarlet letter as a badge of our undying need to deliver services to you on time, in budget, and beyond your expectations. If that ends up leading to heart disease….well, we’ll live with that. If our service prevents your heart attacks, then we’ve done our job.</p>
  </section>
</body>
</html>
```